Pivots & Treads .com

This website is simple!!!
Landing page background image should capture the customers attention!!! We will provide a image as a example of what we like. The purpose for this website is to provide customers with a clean easy way to request a quote for industrial casters and wheels by OEM’s as well as maintenance departments worldwide. Please see if you can follow our thought process below.
Customer comes to website, they are invited to Request a Quote by providing us with Manufacturer Name, Manufacturers Part # and quantity needed.
If this is not known the customer will complete will WP conversation format form answering about 10 questions
Or
Look up the part number in one of the 8 to 12 catalogs located in the Flippin Book format on our catalog page, or equal plug in .
When the client request a quote a account page will pop up request The following:
Clients first and last name
Email address
And optional questions
Company name and best contact number.
Once this is complete customer will hit SUBMIT.
The customers request will be in system. A email will be sent to Customer service notifying us the Quote Request has been made.
We will then build a quote for the customer with a good, better and best options. Customers Request a Quote submission may have more than one caster or wheel requested at a time, so website must allow this.
When the customer comes back into website there email address will come up as the account name and request a password be made for them. This will allow them to store quotes in their account for future needs. If quote is older than 30 day the system will trigger a button at the bottom of the quote for resubmit Request for updated quote.
Once customer reviews quote the quote can be Converted to order within the website.
Once Converted the system will send us a email and order will be processed.
We will need a Chat program that will text to CS the questions.
You will need to have high quality graphic design skills on your team.
We have found 2 plugins that would work nicely with our new website Flippin books to showcase our catalogs for customers to research and WPForms conversation forms to complete request for quote form.
Just Ideas:
Very very ghosted caster blueprint in white background but very very ghosted or the icon just idea
We have never had a font used we like
Grayscale every except for rubber on wheels and logo icon
Website should have hamburger menu on left
Website should hav responsive deign
Account head on right side
Has anyone read the brief from top to bottom and the updates, I’m seeing a lot of duplicates of the website I posted in images I want a clean website With lite backgrand with the poly being definite colors on each wheel I added a green yellow and red image has anyone looked at that Just a question?
Went on vacation/holiday

```html
<!DOCTYPE html>
<html lang="en">
<head>
<meta charset="utf-8">
<title>Pivots &amp; Treads — Landing Page</title>
<link href="https://fonts.googleapis.com/css2?family=Fira+Sans:wght@400;500;600&family=Viga&display=swap" rel="stylesheet">
<style>
  :root{
    --brand:#294598;
    --grey:#cbcbcb;
    --white:#ffffff;
    --board:#eeeeee;
    --page:#f7f7f8;
    --ink:#555a63;
    --soft:#8a8f98;
    --rule:#e6e7ea;
  }
  *{box-sizing:border-box;margin:0;padding:0}
  html,body{width:1037px;height:1200px;overflow:hidden;background:var(--board)}
  body{position:relative;font-family:"Fira Sans",sans-serif;color:var(--ink)}

  /* brand board */
  .brand-board{position:absolute;left:0;top:90px;width:1037px;height:150px}
  .brand-name{position:absolute;left:150px;top:38px;width:220px;font-family:"Viga",sans-serif;font-size:27px;line-height:1.15;color:var(--brand)}
  .board-divider{position:absolute;top:20px;width:1px;height:110px;background:var(--grey)}
  .board-divider.one{left:400px}
  .board-divider.two{left:590px}
  .board-heading{position:absolute;top:16px;font-family:"Viga",sans-serif;font-size:24px;color:var(--brand)}
  .fonts{left:440px}
  .colors{left:640px}
  .font-sample{position:absolute;left:440px;color:#777}
  .font-sample.display{top:78px;font-family:"Viga",sans-serif;font-size:20px}
  .font-sample.body{top:108px;font-size:12px}
  .swatches{position:absolute;left:640px;top:70px;display:flex;gap:10px}
  .swatch{width:32px;text-align:center;font-size:7px;color:#555}
  .swatch i{display:block;width:32px;height:32px;border-radius:50%;margin-bottom:6px}

  /* screens */
  .screen{position:absolute;top:330px;height:454px;background:var(--page);box-shadow:0 2px 10px rgba(0,0,0,.06);overflow:hidden}
  .screen.desktop{left:31px;width:726px}
  .screen.mobile{left:787px;width:218px}

  .menu-block{position:absolute;left:0;top:0;background:var(--brand);display:flex;align-items:center;justify-content:center}
  .desktop .menu-block{width:53px;height:54px}
  .mobile .menu-block{width:36px;height:36px}
  .menu-block span{display:block;height:1.3px;background:var(--white);margin:3px 0}
  .menu-icon{width:14px}
  .menu-icon span:nth-child(2){width:10px}
  .menu-icon span:nth-child(3){width:12px}

  .rule-h{position:absolute;left:0;right:0;height:1px;background:var(--rule)}
  .rule-v{position:absolute;top:0;bottom:0;width:1px;background:var(--rule)}

  .nav-name{position:absolute;font-family:"Viga",sans-serif;color:var(--brand)}
  .desktop .nav-name{left:97px;top:20px;font-size:12px}
  .mobile .nav-name{left:36px;right:36px;top:12px;font-size:10px;text-align:center}
  .contact{position:absolute;left:517px;top:22px;font-size:6.5px;color:var(--soft);letter-spacing:.2px}
  .account{position:absolute;width:9px;height:10px}
  .desktop .account{left:692px;top:22px}
  .mobile .account{left:199px;top:13px}

  .social{position:absolute;left:24px;top:211px;display:flex;flex-direction:column;gap:12px}
  .social i{display:block;width:7px;height:7px;border-radius:50%;background:#b9bcc2}
  .social i.active{background:var(--brand)}
  .copyright{position:absolute;left:692px;top:205px;writing-mode:vertical-rl;font-size:6px;color:var(--soft);letter-spacing:.3px}

  .eyebrow{position:absolute;left:98px;top:144px;display:flex;align-items:center;font-size:7px;letter-spacing:4px;color:var(--soft)}
  .eyebrow::before{content:"";display:block;width:40px;height:1px;background:#c4c6cb;margin-right:8px}
  .hero-title{font-family:"Viga",sans-serif;color:var(--brand);font-weight:400;line-height:1}
  .desktop .hero-title{position:absolute;left:97px;top:157px;font-size:31px}
  .tagline{color:var(--ink)}
  .desktop .tagline{position:absolute;left:98px;top:200px;font-size:9.4px}
  .steps-lead{color:var(--ink)}
  .desktop .steps-lead{position:absolute;left:98px;top:237px;font-size:8.6px}
  .steps{list-style:none}
  .desktop .steps{position:absolute;left:98px;top:260px}
  .steps li{position:relative;padding-left:9px;font-size:7.4px;color:var(--ink);height:19.5px}
  .steps li::before{content:"";position:absolute;left:0;top:2.5px;width:3px;height:3px;border-right:1.2px solid var(--brand);border-top:1.2px solid var(--brand);transform:rotate(45deg)}
  .actions{display:flex;gap:7px}
  .desktop .actions{position:absolute;left:97px;top:335px}
  .btn{display:flex;align-items:center;justify-content:center;width:77px;height:28px;font-size:6.6px;font-weight:600;letter-spacing:.2px;text-transform:uppercase}
  .btn.primary{background:var(--brand);color:var(--white)}
  .btn.secondary{background:var(--white);color:var(--brand);border:1px solid #c9ccd3}

  .hero-photo{position:absolute;border-radius:6px;background:radial-gradient(ellipse at 30% 35%,#e4e5e7 0%,#cfd1d4 32%,transparent 55%),radial-gradient(ellipse at 70% 65%,#2f4da3 0%,#294598 30%,#3a3f4b 45%,transparent 62%),#f1f1f2}
  .desktop .hero-photo{left:349px;top:140px;width:281px;height:227px}
  .mobile .hero-photo{left:29px;top:79px;width:162px;height:140px}

  .mobile .hero-title{position:absolute;left:0;right:0;top:232px;font-size:21px;text-align:center}
  .mobile .tagline{position:absolute;left:0;right:0;top:273px;font-size:8.6px;text-align:center}
  .mobile .steps-lead{position:absolute;left:29px;top:295px;font-size:8.6px}
  .mobile .steps{position:absolute;left:29px;top:318px}
  .mobile .actions{position:absolute;left:28px;top:382px;gap:7px}
  .mobile .btn{width:78px;height:28px;font-size:6.4px}
</style>
</head>
<body>

<section class="brand-board">
  <div class="brand-name">Pivots &amp; Treads .com</div>
  <div class="board-divider one"></div>
  <h2 class="board-heading fonts">Fonts:</h2>
  <div class="font-sample display">Viga</div>
  <div class="font-sample body">Fira Sans</div>
  <div class="board-divider two"></div>
  <h2 class="board-heading colors">Colors:</h2>
  <div class="swatches">
    <div class="swatch"><i style="background:var(--brand)"></i>#294598</div>
    <div class="swatch"><i style="background:var(--grey)"></i>#cbcbcb</div>
    <div class="swatch"><i style="background:var(--white)"></i>#ffffff</div>
  </div>
</section>

<main class="screen desktop">
  <div class="rule-h" style="top:54px"></div>
  <div class="rule-v" style="left:53px"></div>
  <div class="rule-v" style="left:667px"></div>
  <div class="menu-block"><div class="menu-icon"><span></span><span></span><span></span></div></div>
  <div class="nav-name">Pivots &amp; Treads</div>
  <div class="contact">+1 234 568 809 &nbsp;&nbsp;|&nbsp;&nbsp; info@example.com</div>
  <svg class="account" viewBox="0 0 10 11" aria-label="Account"><circle cx="5" cy="3" r="2.6" fill="#9a9ea6"/><path d="M0 11c0-3.5 2.2-5 5-5s5 1.5 5 5z" fill="#9a9ea6"/></svg>

  <div class="social"><i></i><i class="active"></i><i></i></div>
  <div class="copyright">Copyright © 2022 - PivotsTreads</div>

  <div class="eyebrow">WELCOME TO</div>
  <h1 class="hero-title">Pivots &amp; Treads</h1>
  <p class="tagline">#1 Solutions for all your applications</p>
  <p class="steps-lead">As easy as 1-2-3</p>
  <ul class="steps">
    <li>Request a Quote</li>
    <li>Receive a Quote</li>
    <li>Convert a Quote to order</li>
  </ul>
  <div class="actions">
    <a class="btn primary">Request a Quote</a>
    <a class="btn secondary">Our Catalog</a>
  </div>
  <div class="hero-photo" role="img" aria-label="Photo of a grey cast-iron wheel and a swivel caster with a blue polyurethane tread"></div>
</main>

<main class="screen mobile">
  <div class="rule-h" style="top:36px"></div>
  <div class="rule-v" style="left:182px;bottom:auto;height:36px"></div>
  <div class="menu-block"><div class="menu-icon" style="width:11px"><span></span><span></span><span></span></div></div>
  <div class="nav-name">Pivots &amp; Treads</div>
  <svg class="account" viewBox="0 0 10 11" aria-label="Account"><circle cx="5" cy="3" r="2.6" fill="#9a9ea6"/><path d="M0 11c0-3.5 2.2-5 5-5s5 1.5 5 5z" fill="#9a9ea6"/></svg>

  <div class="hero-photo" role="img" aria-label="Photo of a grey cast-iron wheel and a swivel caster with a blue polyurethane tread"></div>
  <h1 class="hero-title">Pivots &amp; Treads</h1>
  <p class="tagline">#1 Solutions for all your applications</p>
  <p class="steps-lead">As easy as 1-2-3</p>
  <ul class="steps">
    <li>Request a Quote</li>
    <li>Receive a Quote</li>
    <li>Convert a Quote to order</li>
  </ul>
  <div class="actions">
    <a class="btn primary">Request a Quote</a>
    <a class="btn secondary">Our Catalog</a>
  </div>
</main>

</body>
</html>
```